Student Profile

I would like to create a profile of .a few scholars at a primary school in South Africa. The profile is attached. I would like to it to be visually appealing for donors and to be in the same vein as the Thabeng College PDF. Please also find our branding guide and our logo. I've also included a few pictures that I would like for you to include.

Target Market(s)

Potential donors

Industry/Entity Type

School

Requirements
Must have
• Colours from the branding guide, photos

```html
<!DOCTYPE html>
<html lang="en">
<head>
<meta charset="utf-8">
<title>Thabeng College – Scholar Profile</title>
<link href="https://fonts.googleapis.com/css2?family=Didact+Gothic&display=swap" rel="stylesheet">
<style>
  :root{
    --backdrop:#d6d6d6;
    --wood-dark:#4a3a2e;
    --wood-mid:#6b5646;
    --wood-light:#7d6756;
    --sheet:#ffffff;
    --ink:#2b2b2b;
    --brand-blue:#1f8fd6;
    --footer-ink:#ffffff;
    --photo-a:#8a6a55;
    --photo-b:#b5443c;
    --photo-c:#3d4f73;
  }
  *{box-sizing:border-box;margin:0;padding:0}
  html,body{width:1200px;height:794px;overflow:hidden}
  body{
    background:radial-gradient(ellipse at center,#e6e6e6 0%,var(--backdrop) 70%);
    font-family:"Didact Gothic",sans-serif;
    color:var(--ink);
  }
  .flyer{
    position:absolute;left:320px;top:12px;width:560px;height:770px;
    background:
      repeating-linear-gradient(90deg,rgba(0,0,0,.08) 0 2px,transparent 2px 9px,rgba(255,255,255,.04) 9px 11px,transparent 11px 17px),
      linear-gradient(90deg,var(--wood-dark),var(--wood-mid) 40%,var(--wood-light) 60%,var(--wood-mid));
    box-shadow:0 6px 18px rgba(0,0,0,.25);
  }
  .story-panel{
    position:absolute;left:44px;top:28px;width:472px;height:636px;
    background:var(--sheet);
    padding:20px 22px 0 24px;
  }
  .story-panel p{font-size:10px;line-height:1.3;margin-bottom:10px}
  .quote-credit{display:block}
  .brand{
    position:absolute;left:24px;bottom:14px;display:flex;align-items:center;gap:8px;
  }
  .brand-dot{width:22px;height:22px;border-radius:50%;background:var(--brand-blue)}
  .brand-name{font-size:13px;color:var(--brand-blue);letter-spacing:.5px;text-transform:uppercase}
  .scholar-photo{
    position:absolute;right:28px;top:572px;width:172px;height:138px;
    background:var(--sheet);padding:5px;box-shadow:0 3px 8px rgba(0,0,0,.35);
  }
  .scholar-photo div{
    width:100%;height:100%;
    background:linear-gradient(120deg,var(--photo-a) 0%,var(--photo-b) 45%,var(--photo-c) 100%);
  }
  .contact-list{
    position:absolute;left:44px;top:680px;list-style:none;
    color:var(--footer-ink);font-size:13px;
  }
  .contact-list li{display:flex;align-items:center;gap:10px;margin-bottom:4px}
  .contact-list svg{width:16px;height:16px;flex:none}
</style>
</head>
<body>
  <article class="flyer">
    <section class="story-panel">
      <p>“I was always number one in my class, and I especially loved accounting, but my mother didn’t really understand,” says Lerato. Lerato grew up hungry and said she didn’t get much adult support and encouragement. She dropped out in Grade 10, but still looked for piece work to support her studies. Lerato moved to Johannesburg from Limpopo with her partner at the time to seek a new life. It was harder than she expected, compounded by her partner’s incapacity to work due to illness. Lerato supported them both on a domestic worker’s salary.</p>
      <p>Tenacious little Zola loves her mom and cherishes the time they spend reading books and doing Zola’s math homework. “My mom tells me I can be anything I want to be.”</p>
      <p>Indeed, Zola wants to be many things. She wants to be a chef to help her mom with the cooking and, she wants to teach. She says her students will attend Ubuntu Heights University after they finish school! Currently, Zola enjoys helping other scholars with their class work, especially those struggling with math.</p>
      <p>After Zola herself completes her university studies, she wants to live in Cape Town. “Cape Town makes me feel very happy,” she says.</p>
      <p>A university preparatory school located in the Alexandra Township of Johannesburg, South Africa, Thabeng College not only equips its scholars with the tools they need to achieve academic success, but also provides them with the skills necessary to succeed in life. This includes intentionally creating a nurturing and enabling environment where respect for oneself and others, self-confidence, and resiliency are equally developed and valued alongside the key learning and academic skills that are foundational for students on the path to university. “Thabeng College was founded so that children like Zola can dream with their eyes wide opened! We are delighted to watch Zola and her peers grow into such thoughtful and intelligent little beings”, says Thabeng College co-founder Amira Dlamini-Khoza.</p>
      <p>“Zola shows compassion to other scholars. She says “sorry” if someone feels sad. She is also very curious, she’s always asking questions in class.”<span class="quote-credit">Sipho, Grade 1 Scholar</span></p>
      <p style="width:300px">“Zola demonstrates excellence in her school work. She displays grit and tries until she gets it right. She is loving, shows compassion, and invites other scholars to play with her. She is one of the top scholars in my class – always eager to learn new things and is excellent at solving problems and overcoming challenges.”<span class="quote-credit">Ms Dudu, Grade 1 Teacher</span></p>
      <div class="brand">
        <span class="brand-dot"></span>
        <span class="brand-name">Thabeng College</span>
      </div>
    </section>
    <figure class="scholar-photo"><div role="img" aria-label="Photo of a scholar with her mother outside the school"></div></figure>
    <ul class="contact-list">
      <li><svg viewBox="0 0 16 16"><circle cx="8" cy="8" r="8" fill="#1f8fd6"/><path d="M5.5 4.5l1.5 0 .7 2-1 .8a5 5 0 0 0 2 2l.8-1 2 .7v1.5c-3.5.5-6.5-2.5-6-6z" fill="#fff"/></svg>+27 11 555 0142</li>
      <li><svg viewBox="0 0 16 16"><circle cx="8" cy="8" r="8" fill="#1f8fd6"/><rect x="4" y="5.5" width="8" height="5.5" fill="none" stroke="#fff"/><path d="M4 5.5l4 3 4-3" fill="none" stroke="#fff"/></svg>giving@thabengcollege.org</li>
      <li><svg viewBox="0 0 16 16"><circle cx="8" cy="8" r="8" fill="#1f8fd6"/><circle cx="8" cy="8" r="4" fill="none" stroke="#fff"/><path d="M4 8h8M8 4v8" stroke="#fff"/></svg>www.thabengcollege.org</li>
    </ul>
  </article>
</body>
</html>
```